Cover needed for book, Wedded to the Fellow Who Drifted Out to Sea

Cover should use the attached photograph, with the groom faded in some way, to represent the concept in the title. Overall look should tell readers the book is in the genre of Marian's Embers, Never Send Us Back Home etc. Book is memoir of Edith, who was married to a man who had obsessive-compulsive disorder when little was known about the condition.

Text should be

Wedded to the Fellow Who Drifted Out to Sea
The true story of how obsession tore a family apart
By Edith Harcombe

```html
<!DOCTYPE html>
<html lang="en">
<head>
<meta charset="utf-8">
<title>Wedded to the Fellow Who Drifted Out to Sea — Cover</title>
<link rel="stylesheet" href="https://fonts.googleapis.com/css2?family=Anton&family=Nothing+You+Could+Do&family=Arimo&display=swap">
<style>
  :root {
    --cyan: #5ffaff;
    --cyan-soft: rgba(60, 235, 250, 0.75);
    --ink: #111418;
    --navy: #0d4a70;
    --paper: #ffffff;
    --placeholder: #eff3f6;
    --placeholder-text: #b9bdc1;
  }
  * { margin: 0; padding: 0; box-sizing: border-box; }
  html, body { width: 1200px; height: 823px; overflow: hidden; background: var(--paper); }
  .cover { position: relative; width: 1200px; height: 823px; background: var(--paper); overflow: hidden; }

  .wash { position: absolute; border-radius: 50%; filter: blur(6px); }
  .wash--back { left: 400px; top: 110px; width: 260px; height: 440px;
    background: radial-gradient(ellipse at center, var(--cyan-soft) 0%, rgba(60,235,250,0.45) 55%, rgba(60,235,250,0) 75%); }
  .wash--spine { left: 560px; top: 0; width: 380px; height: 360px;
    background: radial-gradient(ellipse at center, rgba(60,235,250,0.55) 0%, rgba(60,235,250,0.3) 55%, rgba(60,235,250,0) 75%); }
  .wash--bottom { left: 640px; top: 600px; width: 560px; height: 240px;
    background: radial-gradient(ellipse at center, rgba(60,235,250,0.6) 0%, rgba(60,235,250,0.3) 55%, rgba(60,235,250,0) 75%); }

  .band { position: absolute; left: 0; width: 585px; background: var(--cyan); }
  .band--top { top: 0; height: 122px; }
  .band--bottom { top: 725px; height: 98px; }

  .author-portrait { position: absolute; left: 197px; top: 197px; width: 214px; height: 283px;
    background: var(--placeholder); box-shadow: 0 1px 4px rgba(0,0,0,0.2);
    display: flex; align-items: center; justify-content: center; overflow: hidden; }
  .author-portrait span { font-family: "Arimo", sans-serif; font-size: 30px; color: var(--placeholder-text);
    transform: rotate(-56deg); white-space: nowrap; }

  .script { font-family: "Nothing You Could Do", cursive; color: var(--ink); }
  .tagline { position: absolute; left: 60px; top: 500px; width: 462px; font-size: 28px; line-height: 42px; }
  .tagline .line { display: block; white-space: nowrap; }
  .tagline .byline { text-align: right; }

  .isbn { position: absolute; left: 353px; top: 733px; font-family: "Arimo", sans-serif; font-size: 12px; color: var(--ink); word-spacing: 4px; }

  .spine { position: absolute; left: 585px; top: 120px; width: 40px; height: 620px;
    writing-mode: vertical-rl; font-size: 19px; line-height: 40px; white-space: nowrap; }
  .spine .spine-author { margin-top: 34px; }

  .front-author { position: absolute; left: 690px; top: 84px; width: 450px; text-align: center;
    font-family: "Nothing You Could Do", cursive; color: var(--navy); font-size: 28px; white-space: nowrap; }

  .wedding-photo { position: absolute; left: 770px; top: 195px; width: 325px; height: 430px;
    border-radius: 46% 46% 40% 40% / 30% 30% 25% 25%;
    background: linear-gradient(90deg, #2ee4fb 0%, #33c8f2 38%, #c9d2d8 55%, #eceff1 80%, #ffffff 100%); }

  .title { position: absolute; left: 690px; top: 622px; width: 480px; font-family: "Anton", sans-serif;
    color: var(--navy); text-transform: uppercase; line-height: 1; }
  .title .line { display: block; white-space: nowrap; }
  .title .big { font-size: 50px; letter-spacing: 0.5px; }
  .title .small { font-size: 26px; margin: 0 4px; }
  .title .line + .line { margin-top: 8px; }
</style>
</head>
<body>
<main class="cover">
  <div class="wash wash--back"></div>
  <div class="wash wash--spine"></div>
  <div class="wash wash--bottom"></div>

  <section class="back-cover">
    <div class="band band--top"></div>
    <div class="author-portrait"><span>author portrait</span></div>
    <p class="tagline script">
      <span class="line">The true story of how obsession</span>
      <span class="line">tore a family apart</span>
      <span class="line byline">by Edith Harcombe</span>
    </p>
    <div class="band band--bottom"></div>
    <p class="isbn">ISBN 0-000-0000-0 $0.00</p>
  </section>

  <section class="spine script">
    <span class="spine-title">Wedded to the Fellow Who Drifted Out to Sea</span>
    <span class="spine-author">by Edith Harcombe</span>
  </section>

  <section class="front-cover">
    <p class="front-author">True Story by Edith Harcombe</p>
    <div class="wedding-photo" role="img" aria-label="Vintage wedding photograph of a bride and groom under a lattice arch, the groom washed out in cyan"></div>
    <h1 class="title">
      <span class="line"><span class="big">Wedded</span><span class="small">to the</span><span class="big">Fellow</span><span class="small">who</span></span>
      <span class="line"><span class="big">Drifted Out to Sea</span></span>
    </h1>
  </section>
</main>
</body>
</html>
```